Business Card design for new private practice opening

I need a business card design for my new private practice with my new logo uploaded as a file
On the front the logo
On the back: maybe a small logo somewhere?
Priv. Doz. DDr. Corinna Vestaluk
Fachärztin für Allgemein- & Viszeralchirurgie
Address: xxx
Tel: xxx
Mobil:xxx
Webseite:xxx
Email:xxx

Contact Information for Business Card

See project description above for details

Requirements
Nice to have
• I would like the colors of the logo incorporated into the business card

```html
<!DOCTYPE html>
<html lang="de">
<head>
<meta charset="utf-8">
<title>Vestaluk Chirurgie – Visitenkarte</title>
<link href="https://fonts.googleapis.com/css2?family=Montserrat:wght@400;500;600&display=swap" rel="stylesheet">
<style>
  :root {
    --stage: #2b2b2e;
    --teal: #45b8b6;
    --card-light: #ececec;
    --card-grey: #8e8e8e;
    --grey-soft: #a3a3a3;
    --ink: #1e1e1e;
    --ink-soft: #4a4a4a;
    --white: #ffffff;
  }
  * { box-sizing: border-box; margin: 0; padding: 0; }
  html, body { width: 1200px; height: 947px; overflow: hidden; }
  body {
    background: var(--stage);
    font-family: "Montserrat", sans-serif;
    display: flex;
    flex-direction: column;
    align-items: center;
    justify-content: center;
    gap: 30px;
  }
  .card {
    position: relative;
    width: 760px;
    height: 434px;
    border-radius: 22px;
    overflow: hidden;
  }

  /* Front */
  .card-front { background: var(--card-grey); }
  .front-pattern {
    position: absolute; inset: 0;
    background: linear-gradient(120deg, #7e7e7e 0%, #9a9a9a 45%, #b4b4b4 75%, #9c9c9c 100%);
  }
  .front-brand {
    position: absolute;
    left: 430px; top: 170px;
    display: flex; align-items: center; gap: 16px;
  }
  .brand-dot {
    width: 74px; height: 74px; border-radius: 50%;
    background: var(--teal);
    border: 4px solid var(--white);
  }
  .brand-name {
    color: var(--white);
    font-weight: 600;
    font-size: 26px;
    line-height: 1.1;
    letter-spacing: 0.5px;
    text-transform: uppercase;
  }

  /* Back */
  .card-back { background: var(--card-light); }
  .back-band {
    position: absolute; left: 0; top: 0; bottom: 0; width: 200px;
    background: var(--card-grey);
  }
  .back-mark {
    position: absolute; left: 110px; top: 170px;
    width: 180px; height: 180px; border-radius: 50%;
    background: var(--teal);
    border: 10px solid var(--white);
    box-shadow: 0 0 0 5px var(--card-grey);
  }
  .back-mark-name {
    position: absolute; left: 80px; top: 372px; width: 240px;
    text-align: center;
    color: var(--teal);
    font-weight: 600; font-size: 15px; letter-spacing: 0.5px;
    text-transform: uppercase;
  }
  .identity { position: absolute; left: 300px; top: 42px; width: 430px; }
  .person-name {
    color: var(--teal); font-weight: 600; font-size: 25px; white-space: nowrap;
  }
  .person-title {
    color: var(--ink-soft); font-size: 15px; margin-top: 6px; white-space: nowrap;
  }
  .divider { height: 1px; background: var(--teal); margin-top: 18px; }
  .contacts {
    position: absolute; left: 312px; top: 150px;
    list-style: none;
    font-size: 18px; color: var(--ink); line-height: 30px;
  }
  .contacts li { display: flex; align-items: center; gap: 14px; }
  .contacts svg { width: 15px; height: 15px; flex: none; }
  .address {
    position: absolute; left: 341px; top: 292px;
    font-size: 18px; line-height: 30px; color: var(--ink); font-style: normal;
  }
</style>
</head>
<body>

  <section class="card card-front" aria-label="Vorderseite">
    <div class="front-pattern" role="img" aria-label="Repeating embossed emblem pattern in soft grey tones"></div>
    <div class="front-brand">
      <span class="brand-dot"></span>
      <span class="brand-name">Vestaluk<br>Chirurgie</span>
    </div>
  </section>

  <section class="card card-back" aria-label="Rückseite">
    <div class="back-band"></div>
    <div class="back-mark"></div>
    <div class="back-mark-name">Vestaluk Chirurgie</div>

    <div class="identity">
      <h1 class="person-name">Priv. Doz. DDr. Corinna Vestaluk</h1>
      <p class="person-title">Fachärztin für Allgemein- &amp; Viszeralchirurgie</p>
      <div class="divider"></div>
    </div>

    <ul class="contacts">
      <li>
        <svg viewBox="0 0 16 16" aria-hidden="true"><rect x="4" y="1.5" width="8" height="13" rx="1.5" fill="none" stroke="var(--teal)" stroke-width="1.4"/></svg>
        555-214-3098
      </li>
      <li>
        <svg viewBox="0 0 16 16" aria-hidden="true"><path d="M3 2.5l3 0 1 3-1.6 1.2a8 8 0 0 0 3.9 3.9L10.5 9l3 1v3c-6 .5-11-4.5-10.5-10.5z" fill="var(--teal)"/></svg>
        555 760-2831
      </li>
      <li>
        <svg viewBox="0 0 16 16" aria-hidden="true"><rect x="1.5" y="3.5" width="13" height="9" fill="var(--teal)"/><path d="M1.5 3.5L8 9l6.5-5.5" fill="none" stroke="var(--white)" stroke-width="1.2"/></svg>
        corinna@vestalukchirurgie.com
      </li>
      <li>
        <svg viewBox="0 0 16 16" aria-hidden="true"><circle cx="8" cy="8" r="6.5" fill="none" stroke="var(--teal)" stroke-width="1.3"/><ellipse cx="8" cy="8" rx="3" ry="6.5" fill="none" stroke="var(--teal)" stroke-width="1.1"/><path d="M1.5 8h13" stroke="var(--teal)" stroke-width="1.1"/></svg>
        www.vestalukchirurgie.com
      </li>
    </ul>

    <address class="address">418 Alder Brook Lane<br>Millford, MI 49012</address>
  </section>

</body>
</html>
```